Web Design Project

Please take a look at my current aged website www.marlowpeoplesupport.example and my newly designed logo and business cards. I would like a new fresh updated look to my website and my new designs incorporated.
Updates

  Good Morning Everyone

Due to an Austrralian licencing issue I have had to have my logo slightly redesigned.

Would you please be able to look at the newly uploaded files and revise your designs.

Thanks so much.  I am very happy with the calibre and quality of the designs so far.

kind Regards

Tessa

Industry/Entity Type

Business

Requirements
Must have
• the exisiting pages and fresh new graphics and a real commitment to my palette of lime green, turqouise and black.

```html
<!DOCTYPE html>
<html lang="en">
<head>
<meta charset="utf-8">
<title>Marlow HR Consulting</title>
<link href="https://fonts.googleapis.com/css2?family=Arimo:wght@400;700&family=Ubuntu:wght@400&display=swap" rel="stylesheet">
<style>
:root{
  --black:#000;
  --turq:#4ec6ec;
  --turq-deep:#2d6f86;
  --lime:#5cb83a;
  --lime-dark:#3f9a24;
  --text:#222;
  --panel-line:#d9f2fb;
  --footer:#2f2f2f;
  --footer-top:#3d3d3d;
  --white:#fff;
}
*{box-sizing:border-box;margin:0;padding:0}
html,body{width:998px;height:1200px;overflow:hidden;background:var(--white);font-family:"Arimo",Arial,sans-serif;color:var(--text)}
.page{position:relative;width:998px;height:1200px}
.abs{position:absolute}
/* header */
.site-header{left:0;top:0;width:998px;height:124px;background:var(--black);border-bottom:3px solid var(--turq)}
.brand{left:52px;top:44px;display:flex;align-items:center;gap:8px}
.brand-dot{width:44px;height:44px;border-radius:50%;border:3px solid var(--turq)}
.brand-name{font-size:20px;color:var(--turq);font-weight:400}
.search{left:755px;top:20px;width:212px;height:26px;background:var(--white);border-radius:5px;font-size:10px;color:#999;padding:7px 10px}
.search svg{position:absolute;right:8px;top:6px}
.main-nav{left:473px;top:72px;width:496px;height:29px;background:var(--turq);border-radius:4px;font-size:13px;overflow:hidden}
.main-nav a{position:absolute;top:0;color:#111;text-decoration:none;line-height:29px;white-space:nowrap}
.main-nav a.active{left:0;width:88px;text-align:center;background:var(--lime);color:var(--white);border-radius:4px 0 0 4px}
/* hero */
.hero-band{left:0;top:127px;width:998px;height:340px;background:var(--turq)}
.slider-frame{left:51px;top:160px;width:898px;height:372px;background:var(--white);box-shadow:0 4px 10px rgba(0,0,0,.25)}
.slide{left:67px;top:176px;width:869px;height:335px;background:linear-gradient(120deg,#e8f7fd 0%,#7ec3ea 35%,#c4e3f5 60%,#eef3f8 100%)}
.slide-caption{left:67px;top:466px;width:869px;height:45px;background:rgba(40,40,40,.72);color:var(--white);font-family:"Ubuntu",sans-serif;font-size:19px;line-height:45px;padding-left:27px;white-space:nowrap}
.phone-ribbon{left:51px;top:158px;width:100px;height:100px;overflow:hidden}
.phone-ribbon span{position:absolute;left:-30px;top:32px;width:170px;height:26px;background:var(--lime);color:var(--white);font-weight:700;font-size:13px;line-height:26px;text-align:center;transform:rotate(-45deg)}
.arrow{top:303px;width:36px;height:38px;background:#3a3a3a;border-radius:50%}
.arrow svg{position:absolute;top:13px}
.dots{left:509px;top:546px;display:flex;gap:5px}
.dots i{width:10px;height:10px;border-radius:50%;background:#8a8a8a}
.dots i.on{background:#1a86c2}
/* sidebar panels */
.panel{background:var(--turq);border-radius:4px;box-shadow:0 1px 4px rgba(0,0,0,.3)}
.panel h3{font-weight:400;font-size:14px;color:#222;padding:9px 0 7px 32px;border-bottom:1px solid var(--panel-line);position:relative}
.panel h3 i{position:absolute;left:8px;top:8px;width:15px;height:18px;border-radius:3px;background:#7a2a1a}
.login{left:56px;top:571px;width:204px;height:164px}
.field{position:absolute;left:25px;width:166px;height:25px;background:var(--white);border-radius:4px;font-size:10px;color:#999;padding:6px 14px}
.submit{position:absolute;left:27px;top:128px;width:70px;height:32px;background:#111;color:var(--white);font-size:11px;border-radius:4px;text-align:center;line-height:32px}
.news{left:56px;top:762px;width:204px;height:268px}
.news h3 i{background:#bbb}
.news-item{padding:0 12px 0 13px;font-size:10.5px;line-height:17px;color:#111}
.news-item .date{font-size:11px;margin-bottom:1px}
.news-sep{margin:10px 12px 14px;border-top:1px dotted #333}
.read-more{text-align:right;padding-right:14px;font-size:10.5px;margin-top:14px}
/* content */
.content h2{left:291px;top:596px;font-weight:400;font-size:17px;color:var(--turq-deep);border-bottom:1px dotted #444;padding-bottom:7px;width:339px;white-space:nowrap}
.world-image{left:293px;top:644px;width:246px;height:163px;background:linear-gradient(180deg,#dfe7ef 0%,#9fb0c2 55%,#eef2f6 100%);box-shadow:1px 2px 5px rgba(0,0,0,.4)}
.intro{left:557px;top:646px;width:405px;font-size:12px;line-height:20px}
.intro p+p{margin-top:20px}
.lead{left:283px;top:836px;font-size:15px;color:#222;white-space:nowrap}
.body-copy{left:283px;top:878px;width:690px;font-size:12px;line-height:20px}
.body-copy p+p{margin-top:20px}
.source{left:283px;top:1036px;font-size:15.5px;color:var(--turq-deep);white-space:nowrap}
/* footer */
.site-footer{left:0;top:1086px;width:998px;height:114px;background:var(--footer)}
.footer-top{left:0;top:1086px;width:998px;height:33px;background:var(--footer-top);color:#eee;font-size:11px;line-height:33px;padding-left:30px}
.social{left:32px;top:1143px;display:flex;gap:8px}
.social i{width:26px;height:26px;border-radius:50%;background:#3b78c8}
.social i.rss{background:#e8671c}
.footer-links{right:30px;top:1129px;color:#fff;font-size:11px;white-space:nowrap}
.footer-links span{margin:0 8px}
.copyright{right:28px;top:1160px;color:#fff;font-size:11px;white-space:nowrap}
</style>
</head>
<body>
<div class="page">
  <header class="site-header abs">
    <div class="brand abs"><span class="brand-dot"></span><span class="brand-name">MarlowConsulting</span></div>
    <div class="search abs">Search
      <svg width="16" height="14" viewBox="0 0 16 14"><circle cx="6" cy="6" r="4.5" fill="none" stroke="#bbb" stroke-width="2"/><line x1="9.5" y1="9" x2="14" y2="12.5" stroke="#bbb" stroke-width="2.5"/></svg>
    </div>
    <nav class="main-nav abs">
      <a class="active">Home</a>
      <a style="left:95px">Our Services</a>
      <a style="left:201px">Our Consultants</a>
      <a style="left:324px">Our Fees</a>
      <a style="left:410px">Contact Us</a>
    </nav>
  </header>

  <section class="hero">
    <div class="hero-band abs"></div>
    <div class="arrow abs" style="left:33px"><svg style="left:11px" width="10" height="12" viewBox="0 0 10 12"><path d="M7 1 2 6l5 5" fill="none" stroke="#fff" stroke-width="2.5"/></svg></div>
    <div class="arrow abs" style="left:931px"><svg style="left:14px" width="10" height="12" viewBox="0 0 10 12"><path d="M3 1l5 5-5 5" fill="none" stroke="#fff" stroke-width="2.5"/></svg></div>
    <div class="slider-frame abs"></div>
    <div class="slide abs" role="img" aria-label="Photo of four smiling business professionals in suits against a soft blue abstract background"></div>
    <div class="slide-caption abs">Outsourced Human Resources Solutions and Strategies</div>
    <div class="phone-ribbon abs"><span>0400 000 123</span></div>
    <div class="dots abs"><i></i><i></i><i class="on"></i><i></i><i></i></div>
  </section>

  <aside>
    <div class="panel login abs">
      <h3><i></i>LOGIN</h3>
      <div class="field" style="top:52px">User Name</div>
      <div class="field" style="top:92px">Password</div>
      <div class="submit">SUBMIT</div>
    </div>
    <div class="panel news abs">
      <h3><i></i>LATEST NEWS</h3>
      <div class="news-item" style="margin-top:12px"><div class="date">May 15, 2012</div>Lorem Ipsum is simply dummy text of the printing and typesetting industry. Lorem Ipsum has been industry.</div>
      <div class="news-sep"></div>
      <div class="news-item"><div class="date">May 15, 2012</div>Lorem Ipsum is simply dummy text of the printing and typesetting industry. Lorem Ipsum has been industry.</div>
      <div class="read-more">Read More &gt;&gt;</div>
    </div>
  </aside>

  <main class="content">
    <h2 class="abs">What can Marlow HR Consulting do for me?</h2>
    <div class="world-image abs" role="img" aria-label="Illustration of business people silhouettes standing before a world map"></div>
    <div class="intro abs">
      <p>During these challenging economic times it can be difficult to justify internal human resources management services or support. However as a business owner or Manager you may find that HR support or advice is required from time to time.</p>
      <p>Marlow HR Consulting are an outsourced HR function.&nbsp; We can provide you with that ongoing support, offer solutions and assist you with developing strategies that fit your business and deliver results.</p>
    </div>
    <p class="lead abs">Take a look at Our Services to see how our comprehensive consultancy can add value to your business.</p>
    <div class="body-copy abs">
      <p>By outsourcing some or all of your HR function you will effectively manage your costs, be able to focus on your core business and still have access to professional up-to-date HR advice, systems and processes.</p>
      <p>“According to a recent survey by Carrow &amp; Finch Advisory more than 80% of companies outsource some type of task or project each year.&nbsp; The survey concludes that “by farming out management of operations that are not mission-critical, (these companies) are better able to concentrate on growth, competitors and profitability.&nbsp; If you’re not doing any outsourcing, you might be hurting your business”.</p>
    </div>
    <p class="source abs">Source:&nbsp; The Practical Handbook of Business Outsourcing (Owen Hartley) 2005</p>
  </main>

  <footer>
    <div class="site-footer abs"></div>
    <div class="footer-top abs">Connect with us :</div>
    <div class="social abs"><i></i><i></i><i></i><i class="rss"></i></div>
    <div class="footer-links abs">Privacy Policy<span>|</span>Terms &amp; Conditions<span>|</span>Contact Us</div>
    <div class="copyright abs">Copyright © 2012&nbsp; MarlowConsulting, All Rights Reserved</div>
  </footer>
</div>
</body>
</html>
```